New business card for civil engineering company - "Keystone Audit"

We need a business card designed for our new structural engineering company.

The company name is "Keystone Audit" logo files attached.

We would like the following:
* Two-sided card
* Simple design

Information to be placed on the card:
Name - Marcus Dellow
Job Title - Director / Structural Engineer
Credentials - BEng(Hons), CPEng, CMengNZ, IntPE(NZ)
Email - marcus.dellow@keystoneaudit.co.nz
mobile - 0219364058
website - www.keystoneaudit.co.nz

```html
<!DOCTYPE html>
<html lang="en">
<head>
<meta charset="utf-8">
<title>Keystone Audit – Business Card</title>
<link rel="stylesheet" href="https://fonts.googleapis.com/css2?family=Arimo:wght@700&family=Source+Sans+3:wght@400;600&display=swap">
<style>
  :root {
    --page: #ffffff;
    --navy: #16113f;
    --band-light: #4a5075;
    --band-mid: #34355a;
    --rule: #3c3b35;
    --name-blue: #a9d0f2;
    --title-text: #cfd9ee;
    --contact-text: #c5d6f4;
    --icon-blue: #4a8fd6;
    --brand-grey: #55545a;
    --brand-square: #6fa9e0;
    --brand-square-back: #8f8f93;
    --credentials: #b9bcd0;
  }
  * { margin: 0; padding: 0; box-sizing: border-box; }
  html, body {
    width: 1000px; height: 1200px; overflow: hidden;
    background: var(--page);
    font-family: "Source Sans 3", "Helvetica Neue", Arial, sans-serif;
  }
  .sheet { position: relative; width: 1000px; height: 1200px; }

  .card {
    position: absolute; left: 165px; width: 663px; height: 428px;
    background: var(--navy); overflow: hidden;
  }
  .card--front { top: 115px; }
  .card--back { top: 655px; }

  .brand { position: absolute; display: flex; align-items: center; gap: 10px; }
  .brand__mark { width: 20px; height: 20px; background: var(--brand-square); }
  .brand__name {
    font-weight: 600; font-size: 24px; letter-spacing: 2px; line-height: 1;
    text-transform: uppercase; color: var(--brand-grey); white-space: nowrap;
  }
  .card--front .brand { left: 44px; top: 243px; }
  .card--back .brand {
    left: 0; right: 0; top: 280px; justify-content: center;
  }
  .card--back .brand__name { font-size: 28px; letter-spacing: 3px; }
  .card--back .brand__mark { width: 22px; height: 22px; background: var(--brand-square-back); }

  .holder { position: absolute; right: 22px; top: 226px; text-align: right; }
  .holder__name {
    font-family: "Arimo", Helvetica, Arial, sans-serif; font-weight: 700;
    font-size: 35px; letter-spacing: 3.5px; color: var(--name-blue); line-height: 1;
  }
  .holder__role {
    margin-top: 14px; font-size: 15px; letter-spacing: 2.3px; color: var(--title-text);
  }

  .divider { position: absolute; left: 0; right: 0; top: 302px; height: 7px; background: var(--rule); }

  .contacts { position: absolute; left: 42px; top: 321px; list-style: none; }
  .contacts__item {
    display: flex; align-items: center; height: 32px;
    font-size: 15.5px; color: var(--contact-text); letter-spacing: .2px;
  }
  .contacts__icon { width: 20px; height: 20px; margin-right: 12px; flex: none; }
  .contacts__icon * { stroke: var(--icon-blue); fill: none; stroke-width: 1.4; }

  .decor { position: absolute; inset: 0; }
  .credentials {
    position: absolute; left: 0; right: 0; top: 384px; text-align: center;
    font-size: 16.5px; letter-spacing: .6px; color: var(--credentials);
  }
</style>
</head>
<body>
<main class="sheet">
  <section class="card card--front" aria-label="Card front">
    <div class="brand">
      <span class="brand__mark"></span>
      <span class="brand__name">Keystone Audit</span>
    </div>
    <div class="holder">
      <h1 class="holder__name">Marcus Dellow</h1>
      <p class="holder__role">Director / Structural Engineer</p>
    </div>
    <div class="divider"></div>
    <ul class="contacts">
      <li class="contacts__item">
        <svg class="contacts__icon" viewBox="0 0 20 20" aria-hidden="true">
          <path d="M5 3l3 3-2 2c1 2 3 4 5 5l2-2 3 3-2 2C9 17 3 11 3 5z"/>
          <path d="M12 3a5 5 0 0 1 5 5M12 6a2 2 0 0 1 2 2"/>
        </svg>
        0219364058
      </li>
      <li class="contacts__item">
        <svg class="contacts__icon" viewBox="0 0 20 20" aria-hidden="true">
          <rect x="2" y="5" width="16" height="11"/>
          <path d="M2 5l8 6 8-6M2 16l6-5M18 16l-6-5"/>
        </svg>
        marcus.dellow@keystoneaudit.co.nz
      </li>
      <li class="contacts__item">
        <svg class="contacts__icon" viewBox="0 0 20 20" aria-hidden="true">
          <circle cx="10" cy="10" r="7"/>
          <ellipse cx="10" cy="10" rx="3" ry="7"/>
          <path d="M3 10h14"/>
        </svg>
        www.keystoneaudit.co.nz
      </li>
    </ul>
  </section>

  <section class="card card--back" aria-label="Card back">
    <svg class="decor" viewBox="0 0 663 428" aria-hidden="true">
      <polygon points="0,0 113,0 0,80" fill="var(--band-light)"/>
      <polygon points="113,0 200,0 0,140 0,80" fill="var(--band-mid)"/>
      <polygon points="663,348 663,428 548,428" fill="var(--band-mid)"/>
    </svg>
    <div class="brand">
      <span class="brand__mark"></span>
      <span class="brand__name">Keystone Audit</span>
    </div>
    <p class="credentials">Credentials - BEng(Hons), CPEng, CMengNZ, IntPE(NZ) Harlow Bay, OR 97155</p>
  </section>
</main>
</body>
</html>
```